Income Tax and Accounting Brochure

I need a brochure using my new logo (file attached). I do tax work and accounting work. I am an EA (QVX Enrolled Agent - logo attached) and would like this incorporated into the brochure. I also have a MSA in Accounting. Please incorporate the text that I have provided in the brochure.
Updates

Need extra days to review

Target Market(s)

Tax Clients - both business and individuals

Industry/Entity Type

Accounting

Colors
0054AA
0677BA
7BADD7
CADEEF
E8F1F8

Requirements
Must have
• Use my logo and the QVX EA file in the brochure
Nice to have
• I would like to see a brochure that I can customize with my own text if possible.

```html
<!DOCTYPE html>
<html lang="en">
<head>
<meta charset="utf-8">
<title>Northway Accounting Consulting – Tax Brochure</title>
<link href="https://fonts.googleapis.com/css2?family=Montserrat:wght@400;600;700;800;900&family=Open+Sans:wght@400;600&display=swap" rel="stylesheet">
<style>
:root{
  --navy:#0054AA;
  --blue:#0677BA;
  --sky:#7BADD7;
  --mist:#CADEEF;
  --ice:#E8F1F8;
  --red:#C4122F;
  --ink:#3b4553;
  --page:#ffffff;
  --backdrop:#e9ebee;
}
*{box-sizing:border-box;margin:0;padding:0}
html,body{width:1200px;height:3420px;overflow:hidden;background:var(--backdrop)}
body{position:relative;font-family:"Open Sans",Arial,sans-serif;color:var(--ink)}
.spread{position:absolute;left:40px;width:1120px;height:750px;background:var(--page);box-shadow:0 6px 24px rgba(0,0,0,.12);overflow:hidden}
.spread--outside{top:920px}
.spread--inside{top:1750px}
.panel{position:absolute;top:0;width:373px;height:750px;overflow:hidden}
.panel--1{left:0}.panel--2{left:373px}.panel--3{left:746px}
.fold{position:absolute;top:0;width:1px;height:750px;background:var(--ice)}
.photo{position:absolute;background:linear-gradient(135deg,var(--mist),var(--sky))}
.swoosh{position:absolute;left:0;width:373px}
.heading{font-family:"Montserrat",Arial,sans-serif;font-weight:800;line-height:1.05}
.heading .red{color:var(--red)}
.heading .navy{color:var(--navy)}
.body-copy{font-size:11.5px;line-height:1.55;margin-bottom:10px}
.accent-copy{font-size:12px;line-height:1.5;color:var(--red);font-weight:600;margin-bottom:10px}
.brand{display:flex;align-items:center;gap:8px;font-family:"Montserrat",Arial,sans-serif;font-weight:700;color:var(--navy);font-size:13px;line-height:1.15;text-transform:uppercase}
.brand__dot{width:26px;height:26px;border-radius:50%;background:var(--red);flex:none}
.call-bar{position:absolute;left:40px;right:40px;bottom:30px;display:flex;align-items:center;gap:8px;font-family:"Montserrat",Arial,sans-serif;font-weight:700;font-size:14px;color:var(--navy)}
.call-bar svg{width:18px;height:18px;fill:var(--red)}
.contact{display:flex;align-items:center;gap:10px;font-size:11.5px;margin-bottom:12px}
.contact svg{width:18px;height:18px;fill:var(--blue);flex:none}
.badge-row{display:flex;align-items:center;gap:12px}
.badge{width:70px;height:44px;background:var(--ice);border:2px solid var(--mist)}
.mess-circle{position:absolute;width:170px;height:170px;border-radius:50%;background:var(--red);border:6px solid #fff;display:flex;flex-direction:column;align-items:center;justify-content:center;text-align:center;color:#fff;font-family:"Montserrat",Arial,sans-serif;font-weight:900;line-height:1}
</style>
</head>
<body>

<!-- OUTSIDE SPREAD -->
<section class="spread spread--outside">
  <!-- About panel -->
  <article class="panel panel--1">
    <div class="photo" role="img" aria-label="Portrait photo of the principal accountant smiling in an office" style="left:0;top:0;width:373px;height:250px"></div>
    <svg class="swoosh" style="top:170px" height="140" viewBox="0 0 373 140" aria-hidden="true">
      <path d="M0 60 Q180 10 373 40 L373 140 L0 140Z" fill="#fff"/>
      <path d="M0 70 Q190 18 373 48 L373 62 Q190 36 0 92Z" fill="var(--red)"/>
      <path d="M0 92 Q190 40 373 62 L373 70 Q190 52 0 104Z" fill="var(--navy)"/>
    </svg>
    <div style="position:absolute;left:36px;top:300px;right:30px">
      <h2 class="heading" style="font-size:22px"><span class="red">ABOUT</span><br><span class="navy">MARION T HADLEY,</span></h2>
      <p style="font-size:11px;font-weight:700;color:var(--red);margin:4px 0 12px">MSA EA (PRINCIPAL)</p>
      <p class="body-copy">I hold a Master of Science in Accounting and I am a QVX Enrolled Agent. I also serve as a certified bookkeeping advisor for small firms, including payroll, sales tax and year-end closing for individuals and businesses.</p>
      <p class="body-copy">I have years of experience working with a wide variety of clients, from those who keep neat records to those who need a fresh start. Every return gets my full attention.</p>
      <p class="accent-copy">What a joy it is to watch success in action!</p>
    </div>
  </article>

  <div class="fold" style="left:373px"></div>

  <!-- Back panel -->
  <article class="panel panel--2">
    <div class="badge-row" style="position:absolute;left:50px;top:120px">
      <div class="badge"></div>
      <span class="heading navy" style="font-size:20px;color:var(--navy)">ENROLLED<br>AGENT</span>
    </div>
    <div style="position:absolute;left:50px;top:230px;right:30px">
      <div class="contact"><svg viewBox="0 0 24 24"><path d="M2 5h20v14H2z M2 5l10 8 10-8" fill="none" stroke="var(--blue)" stroke-width="2"/></svg>hello@northwayaccounting.com</div>
      <div class="contact"><svg viewBox="0 0 24 24"><circle cx="12" cy="12" r="9" fill="none" stroke="var(--blue)" stroke-width="2"/><path d="M3 12h18M12 3c4 4 4 14 0 18M12 3c-4 4-4 14 0 18" fill="none" stroke="var(--blue)" stroke-width="1.6"/></svg>www.northwayaccounting.com</div>
      <div class="contact"><svg viewBox="0 0 24 24"><path d="M12 2a7 7 0 0 0-7 7c0 5 7 13 7 13s7-8 7-13a7 7 0 0 0-7-7zm0 9.5A2.5 2.5 0 1 1 12 6.5a2.5 2.5 0 0 1 0 5z"/></svg>48 Harbor Lane, Suite 210,<br>Riverton, adjacent to Main</div>
    </div>
    <svg class="swoosh" style="top:430px" height="200" viewBox="0 0 373 200" aria-hidden="true">
      <path d="M0 20 Q200 -10 373 60 L373 200 L0 200Z" fill="var(--ice)"/>
      <path d="M0 0 Q200 -20 373 40 L373 54 Q200 0 0 18Z" fill="var(--sky)"/>
    </svg>
    <div class="brand" style="position:absolute;left:80px;top:520px;font-size:15px"><span class="brand__dot"></span><span>Northway Accounting<br>Consulting, LLC</span></div>
    <div class="call-bar"><svg viewBox="0 0 24 24"><path d="M6.6 10.8a15 15 0 0 0 6.6 6.6l2.2-2.2a1 1 0 0 1 1-.25 11.4 11.4 0 0 0 3.6.57 1 1 0 0 1 1 1V20a1 1 0 0 1-1 1A17 17 0 0 1 3 4a1 1 0 0 1 1-1h3.5a1 1 0 0 1 1 1c0 1.25.2 2.45.57 3.57a1 1 0 0 1-.25 1z"/></svg>CALL US AT: (555) 014-2290</div>
  </article>

  <div class="fold" style="left:746px"></div>

  <!-- Cover panel -->
  <article class="panel panel--3">
    <div class="brand" style="position:absolute;left:150px;top:40px"><span class="brand__dot"></span><span>Northway Accounting<br>Consulting, LLC</span></div>
    <div class="photo" role="img" aria-label="Photo of a stressed woman at a desk surrounded by stacks of paperwork" style="left:0;top:110px;width:373px;height:270px"></div>
    <svg class="swoosh" style="top:330px" height="120" viewBox="0 0 373 120" aria-hidden="true">
      <path d="M0 40 Q180 90 373 20 L373 120 L0 120Z" fill="#fff"/>
      <path d="M0 30 Q180 80 373 10 L373 24 Q180 92 0 44Z" fill="var(--red)"/>
    </svg>
    <div class="mess-circle" style="left:180px;top:300px">
      <span style="font-size:22px">BOOKS A</span>
      <span style="font-size:38px">MESS</span>
      <span style="font-size:20px;margin-top:4px">NO<br>PROBLEM!</span>
    </div>
    <p class="body-copy" style="position:absolute;left:40px;right:40px;top:500px">We'll prepare your bookkeeping for the year, prepare a Schedule C, as well as your personal income tax return.</p>
    <div class="call-bar"><svg viewBox="0 0 24 24"><path d="M6.6 10.8a15 15 0 0 0 6.6 6.6l2.2-2.2a1 1 0 0 1 1-.25 11.4 11.4 0 0 0 3.6.57 1 1 0 0 1 1 1V20a1 1 0 0 1-1 1A17 17 0 0 1 3 4a1 1 0 0 1 1-1h3.5a1 1 0 0 1 1 1c0 1.25.2 2.45.57 3.57a1 1 0 0 1-.25 1z"/></svg>CALL US AT: (555) 014-2290</div>
  </article>
</section>

<!-- INSIDE SPREAD -->
<section class="spread spread--inside">
  <article class="panel panel--1">
    <div class="photo" role="img" aria-label="Photo of hands working on a calculator with paperwork" style="left:0;top:0;width:373px;height:200px"></div>
    <svg class="swoosh" style="top:130px" height="120" viewBox="0 0 373 120" aria-hidden="true">
      <path d="M0 40 Q200 0 373 50 L373 120 L0 120Z" fill="#fff"/>
      <path d="M0 20 Q200 -20 373 36 L373 54 Q200 6 0 46Z" fill="var(--red)"/>
    </svg>
    <div style="position:absolute;left:36px;top:230px;right:30px">
      <h2 class="heading" style="font-size:12px;color:var(--red);margin-bottom:4px">TAX PREPARATION –</h2>
      <h2 class="heading navy" style="font-size:26px;color:var(--navy);margin-bottom:14px">WHY HIRE US?</h2>
      <p class="body-copy">Preparing your own income tax return can leave you with more questions than answers. According to a study released by the QVX, taxpayers spend many hours on forms. Hiring a professional saves time and brings peace of mind.</p>
      <p class="body-copy">Whether you filed on your own or not, you may be missing credits and deductions you are entitled to. A trained eye finds what software can miss.</p>
      <p class="body-copy">Even if you use a computer program, there is no substitute for the experience of a seasoned tax professional.</p>
    </div>
    <div class="brand" style="position:absolute;left:36px;bottom:70px"><span class="brand__dot"></span><span>Northway Accounting<br>Consulting, LLC</span></div>
    <div class="call-bar" style="left:36px"><svg viewBox="0 0 24 24"><path d="M6.6 10.8a15 15 0 0 0 6.6 6.6l2.2-2.2a1 1 0 0 1 1-.25 11.4 11.4 0 0 0 3.6.57 1 1 0 0 1 1 1V20a1 1 0 0 1-1 1A17 17 0 0 1 3 4a1 1 0 0 1 1-1h3.5a1 1 0 0 1 1 1c0 1.25.2 2.45.57 3.57a1 1 0 0 1-.25 1z"/></svg>CALL US AT: (555) 014-2290</div>
  </article>

  <div class="fold" style="left:373px"></div>

  <article class="panel panel--2">
    <div class="photo" role="img" aria-label="Photo of a laptop keyboard and glasses on a desk" style="left:0;top:0;width:373px;height:170px"></div>
    <svg class="swoosh" style="top:110px" height="110" viewBox="0 0 373 110" aria-hidden="true">
      <path d="M0 50 Q180 10 373 40 L373 110 L0 110Z" fill="#fff"/>
      <path d="M0 40 Q180 0 373 30 L373 44 Q180 16 0 56Z" fill="var(--navy)"/>
    </svg>
    <div style="position:absolute;left:36px;top:210px;right:30px">
      <h2 class="heading" style="font-size:12px;color:var(--red);margin-bottom:4px">HERE'S WHAT YOUR</h2>
      <h2 class="heading" style="font-size:26px;color:var(--navy);margin-bottom:14px">GET...</h2>
      <p class="body-copy">Your tax return will be checked and rechecked by our computer software, identifying potential problems the QVX may look at.</p>
      <p class="body-copy">Our staff will review your return to ensure it is complete and accurate before it is filed.</p>
      <p class="body-copy">Your tax return can be filed electronically, so you will get a refund back quicker.</p>
      <p class="body-copy">Our staff will show you how to adjust your payroll withholding to get more money each paycheck. We give the QVX an honest, clean return.</p>
      <p class="body-copy">We will show you potential deductions to limit your tax liability for next year. In addition, we will give you a sheet of commonly overlooked deductions to track.</p>
    </div>
  </article>

  <div class="fold" style="left:746px"></div>

  <article class="panel panel--3">
    <div style="position:absolute;left:36px;top:50px;right:30px">
      <p class="accent-copy" style="font-size:13px">If you own a small business and haven't kept up your bookkeeping, don't worry.</p>
      <p class="body-copy">We can help you. We'll prepare your bookkeeping for the year, prepare a Schedule C, as well as your personal income tax return.</p>
      <p class="accent-copy">Then we'll help you set up an easy system that allows you to keep your books in tip top shape next year.</p>
    </div>
    <div class="photo" role="img" aria-label="Circular photo of two people shaking hands over a desk" style="left:110px;top:300px;width:180px;height:180px;border-radius:50%;border:6px solid var(--mist)"></div>
    <svg class="swoosh" style="top:560px" height="190" viewBox="0 0 373 190" aria-hidden="true">
      <path d="M0 60 Q200 0 373 40 L373 190 L0 190Z" fill="var(--ice)"/>
      <path d="M0 40 Q200 -20 373 20 L373 34 Q200 0 0 56Z" fill="var(--red)"/>
      <path d="M0 56 Q200 0 373 34 L373 42 Q200 14 0 68Z" fill="var(--navy)"/>
    </svg>
  </article>
</section>

</body>
</html>
```